Dr. Marissa Tevlin Medical/Chiropractic Business Card

Dr. Tevlin is a chiropractor and will require a business card that she uses every single day to book appointments on the back side of the card. Currently the office name goes by Dr. Marissa Tevlin. The chiropractic profession is based on the diagnosis and manipulative treatment of misalignments of the joints, especially those of the spinal column, which are held to cause other disorders by affecting the nerves, muscles, and organs. Dr. Marissa Tevlin is looking for a contemporary and minimalistic design.

Industry/Entity Type

Medical

Contact Information for Business Card

Name: Dr. Marissa Tevlin; Address: 748 Harcastle Rd South, London, ON N5R 2K7; Phone Number: 519.274.6193; Fax: 519.281.5046; email: marissa.tevlin@quorvamail.com

Requirements
Must have
• ability to write multiple appointments date/time on the back of card

```html
<!DOCTYPE html>
<html lang="en">
<head>
<meta charset="utf-8">
<title>Dr. Marissa Tevlin – Business Card</title>
<link href="https://fonts.googleapis.com/css2?family=Arimo:wght@400&family=Libre+Baskerville:wght@700&family=Cinzel:wght@500&display=swap" rel="stylesheet">
<style>
  :root {
    --brand-blue: #00519a;
    --brand-green: #85c226;
    --ink: #1e1e1e;
    --rule: #9a9a9a;
    --card-edge: #6e6e6e;
    --paper: #ffffff;
  }
  * { margin: 0; padding: 0; box-sizing: border-box; }
  html, body {
    width: 1200px; height: 748px; overflow: hidden;
    background: var(--paper);
    font-family: "Arimo", Arial, sans-serif;
    color: var(--ink);
  }
  .canvas { position: relative; width: 1200px; height: 748px; }

  /* Front of card */
  .card-front {
    position: absolute; left: 1px; top: 160px;
    width: 745px; height: 426px;
    border: 1px solid var(--card-edge);
    border-radius: 32px;
    overflow: hidden;
    background: var(--paper);
  }
  .card-front .base-band {
    position: absolute; left: 0; bottom: 0;
    width: 100%; height: 33px;
    background: var(--brand-blue);
  }
  .doctor-name {
    position: absolute; left: 44px; top: 127px;
    font-family: "Libre Baskerville", "Times New Roman", serif;
    font-weight: 700; font-size: 25px;
    color: var(--brand-blue);
    white-space: nowrap;
  }
  .doctor-title {
    position: absolute; left: 44px; top: 169px;
    font-size: 22px;
  }
  .contact-list { position: absolute; left: 40px; top: 284px; list-style: none; }
  .contact-list li {
    display: flex; align-items: center;
    height: 33px; font-size: 22px;
  }
  .contact-list svg { width: 26px; height: 26px; margin-right: 15px; fill: var(--brand-blue); }
  .address {
    position: absolute; left: 386px; top: 284px;
    display: flex; align-items: flex-start;
    font-size: 22px; line-height: 28px;
  }
  .address svg { width: 20px; height: 30px; margin-right: 16px; margin-top: 2px; fill: var(--brand-blue); }

  .practice-mark {
    position: absolute; left: 440px; top: 62px;
    width: 220px;
    display: flex; flex-direction: column; align-items: center;
  }
  .practice-mark .mark-square {
    width: 70px; height: 70px; background: var(--brand-green);
    margin-bottom: 14px;
  }
  .practice-mark .mark-name {
    font-family: "Libre Baskerville", "Times New Roman", serif;
    font-weight: 700; font-size: 20px; color: var(--brand-blue);
    text-align: center; line-height: 26px;
  }

  /* Back of card */
  .card-back {
    position: absolute; left: 772px; top: 1px;
    width: 426px; height: 745px;
    border: 1px solid var(--card-edge);
    border-radius: 32px;
    overflow: hidden;
    background: var(--paper);
  }
  .appointments-header {
    height: 98px; background: var(--brand-blue);
    color: var(--paper);
    font-family: "Cinzel", "Times New Roman", serif;
    font-weight: 500; font-size: 33px; letter-spacing: 5px;
    text-align: center; line-height: 120px;
  }
  .column-label {
    position: absolute; top: 121px;
    font-size: 22px; letter-spacing: 3.5px;
  }
  .column-label.date { left: 32px; }
  .column-label.time { left: 252px; }
  .entry-rule {
    position: absolute; height: 2px; background: var(--rule);
  }
  .entry-rule.date { left: 32px; width: 188px; }
  .entry-rule.time { left: 250px; width: 144px; }
  .reschedule-note {
    position: absolute; left: 0; top: 677px; width: 100%;
    text-align: center; font-size: 16px; line-height: 20px;
  }
</style>
</head>
<body>
<div class="canvas">

  <section class="card-front">
    <div class="practice-mark">
      <div class="mark-square"></div>
      <div class="mark-name">Tevlin Chiropractic</div>
    </div>

    <h1 class="doctor-name">Dr. Marissa Tevlin</h1>
    <p class="doctor-title">Chiropractor</p>

    <ul class="contact-list">
      <li>
        <svg viewBox="0 0 26 26" aria-hidden="true"><path d="M7 1h12a3 3 0 0 1 3 3v18a3 3 0 0 1-3 3H7a3 3 0 0 1-3-3V4a3 3 0 0 1 3-3zm0 3v14h12V4zm6 16.5a1.5 1.5 0 1 0 0 3 1.5 1.5 0 0 0 0-3z"/></svg>
        519.274.6193
      </li>
      <li>
        <svg viewBox="0 0 26 26" aria-hidden="true"><path d="M7 2h11v10H7zm2 2v1.5h7V4zm0 3v1.5h7V7zM3 13h20v7H3zm0 9h20v3H3z"/></svg>
        519.281.5046
      </li>
      <li>
        <svg viewBox="0 0 26 26" aria-hidden="true"><path d="M1 5h24v16H1zm2.5 2 9.5 7.5L22.5 7zM3 19h20L15.5 12.5 13 14.5l-2.5-2z"/></svg>
        marissa.tevlin@quorvamail.com
      </li>
    </ul>

    <div class="address">
      <svg viewBox="0 0 20 30" aria-hidden="true"><path d="M10 0a10 10 0 0 1 10 10c0 7-10 20-10 20S0 17 0 10A10 10 0 0 1 10 0zm0 5a4.5 4.5 0 1 0 0 9 4.5 4.5 0 0 0 0-9z"/></svg>
      <p>748 Harcastle Rd South,<br>London, ON N5R 2K7</p>
    </div>

    <div class="base-band"></div>
  </section>

  <section class="card-back">
    <h2 class="appointments-header">APPOINTMENTS</h2>
    <span class="column-label date">DATE</span>
    <span class="column-label time">TIME</span>

    <div class="entry-rule date" style="top:189px"></div><div class="entry-rule time" style="top:189px"></div>
    <div class="entry-rule date" style="top:240px"></div><div class="entry-rule time" style="top:240px"></div>
    <div class="entry-rule date" style="top:291px"></div><div class="entry-rule time" style="top:291px"></div>
    <div class="entry-rule date" style="top:342px"></div><div class="entry-rule time" style="top:342px"></div>
    <div class="entry-rule date" style="top:394px"></div><div class="entry-rule time" style="top:394px"></div>
    <div class="entry-rule date" style="top:445px"></div><div class="entry-rule time" style="top:445px"></div>
    <div class="entry-rule date" style="top:496px"></div><div class="entry-rule time" style="top:496px"></div>
    <div class="entry-rule date" style="top:547px"></div><div class="entry-rule time" style="top:547px"></div>
    <div class="entry-rule date" style="top:598px"></div><div class="entry-rule time" style="top:598px"></div>
    <div class="entry-rule date" style="top:650px"></div><div class="entry-rule time" style="top:650px"></div>

    <p class="reschedule-note">If you are unable to make your appointment,<br>please call us to reschedule</p>
  </section>

</div>
</body>
</html>
```